Harbour Panels Brochure

Harbour Panels New Brochure Brief
Harbour Panels are manufacturers of kitchen and wardrobe doors. We have 2 target markets, one is business to business and the other business to residential customers.
The main message of our business to residential is to inform them that they can give their kitchen or wardrobe a facelift by just replacing doors and save thousands of dollars by doing this partial renovation. However, this is in direct conflict with our business to business customers (kitchen and wardrobe companies) who buy doors from us and sell complete new kitchens and built in wardrobes to the same residential customers.
Please find links to the Harbour Panels brochure and website below for your reference. The current dimensions of the brochure is approx. 21cmH x 29.7cmW. https://harbourpanels.com.au/harbourpanelsbrochure-2/ https://harbourpanels.com.au/
I would like to keep the layout of the brochure internal pages consistent with the current design, however, I am open to your ideas. The orange colour as seen on the front page should be a dominant theme as it’s based on our logo however not too overpowering, I prefer to cover to be white. I would like a new front page design, changing the door photos (they will be shades of white, not coloured) and also delete the words ‘ultimate door collection’. Heading to be along the lines of “Custom made kitchen and wardrobe doors”.
On the internal pages, some new door designs will be added and some deleted. s. We are thinking of changing all the door colours to shades of white but also stating that Harbour Panels can colour match to any major Australian paint brand.
I would like to include a page for Wardrobe Doors with some photos, text and layout options (photo attached). Please add in the before and after images. Please create a before and after using Mort's kitchen in same layout as wardrobe before and after. Please ensure oven is cut from after image. Please add in the photos attached in this brief.
We would also like to include a FAQs section. Some more text describing our product, such as raw material, thickness of doors, painted or unpainted finish and delivery information is to be added.
Re: the ‘edges’ top of page 3; some will be deleted and one new type of edge will be added.
From page 4 onwards, there are different shapes at the bottom of each door design. We are looking for a new way to communicate this as at the moment it is taking up too much room and people do not readily understand that these door patterns can be supplied in the shapes shown in the little diagrams below them.
Please keep in mind all this information will be given at the time of design. I would like to possibly keep the brochure at 8 pages (as it is now). There may be some other changes along the way as this is still in the preliminary stage. Please include the image of our showroom in the brochure mock up.
I look forward to your reply.
Kind Regards,
Greta
* Please note, the images attach with the individual doors need to be changed to some neutral shades such as white, off white, grey, cream etc (similar to the website: https://harbourpanels.com.au/kitchen-doors/)

```html
<!DOCTYPE html>
<html lang="en">
<head>
<meta charset="utf-8">
<title>Harbour Panels Brochure</title>
<link href="https://fonts.googleapis.com/css2?family=Archivo+Black&family=Montserrat:ital,wght@0,400;0,600;0,700;0,800;1,800&display=swap" rel="stylesheet">
<style>
  :root {
    --orange: #f0a43c;
    --orange-deep: #e58f1f;
    --cream: #f6e3c2;
    --beige: #e9d3b0;
    --ink: #3a3a3a;
    --grey: #8a8a8a;
    --line: #d8b26a;
    --red: #e2322f;
    --door: #dfe5e1;
    --page: #ffffff;
    --backdrop: #ddd6cf;
  }
  * { box-sizing: border-box; margin: 0; padding: 0; }
  html, body { width: 1200px; height: 840px; overflow: hidden; }
  body { background: var(--backdrop); font-family: "Montserrat", sans-serif; color: var(--ink); position: relative; }
  .page { position: absolute; width: 560px; height: 396px; background: var(--page); overflow: hidden; box-shadow: 0 2px 8px rgba(0,0,0,.12); }

  /* cover */
  .cover { left: 320px; top: 16px; }
  .cover svg { position: absolute; inset: 0; }
  .cover-title { position: absolute; right: 28px; top: 172px; text-align: right; font-family: "Archivo Black", sans-serif; font-size: 22px; line-height: 1.05; color: var(--ink); text-transform: uppercase; }
  .cover-tag { position: absolute; left: 230px; top: 316px; font-size: 12px; font-weight: 700; color: var(--ink); }
  .cover-brand { position: absolute; left: 250px; top: 112px; width: 120px; text-align: center; font-family: "Archivo Black", sans-serif; font-size: 15px; line-height: 1.1; color: var(--ink); }

  /* spread */
  .page-left { left: 40px; top: 428px; }
  .page-right { left: 600px; top: 428px; }
  .photo-strip { position: absolute; left: 0; top: 0; width: 100%; height: 46px; background: linear-gradient(90deg, #c8dbe8, #e8595a 45%, #f4f4f4); }
  .benefits { position: absolute; left: 0; top: 46px; width: 220px; height: 310px; background: linear-gradient(180deg, var(--cream), var(--beige)); border-radius: 0 0 60px 0; padding: 56px 12px 10px 14px; }
  .brand { position: absolute; left: 14px; top: 56px; font-family: "Archivo Black", sans-serif; font-size: 14px; line-height: 1.05; }
  .brand small { display: block; font-family: "Montserrat", sans-serif; font-weight: 700; font-size: 8px; }
  .motto { position: absolute; left: 14px; top: 94px; font-size: 7px; font-weight: 600; line-height: 1.3; }
  .benefit-list { list-style: none; margin-top: 36px; font-size: 6.4px; line-height: 1.35; }
  .benefit-list li { margin-bottom: 3px; }
  .benefit-list b { font-weight: 700; }
  .call { margin-top: 6px; font-size: 7.5px; font-weight: 800; }
  .call span { display: block; font-size: 6px; font-weight: 400; }
  .badge { position: absolute; left: 240px; top: 78px; width: 34px; height: 34px; border-radius: 50%; border: 3px solid #2b5ea7; background: #fff; }
  .customise { position: absolute; left: 290px; top: 60px; }
  .customise h2 { font-weight: 800; font-style: italic; font-size: 24px; color: var(--red); line-height: 1; }
  .customise h3 { font-weight: 800; font-style: italic; font-size: 13px; color: var(--ink); margin-left: 50px; }
  .customise p { font-size: 7px; line-height: 1.35; margin-top: 4px; width: 140px; }
  .range { position: absolute; font-size: 6.5px; }
  .range b { font-weight: 800; }
  .doors { position: absolute; display: flex; gap: 10px; }
  .door { width: 58px; display: flex; flex-direction: column; align-items: center; gap: 4px; }
  .door-img { width: 58px; height: 78px; background: var(--door); border: 1px solid #c9d0cc; }
  .door-code { background: var(--orange); color: #fff; font-size: 6.5px; font-weight: 700; padding: 2px 8px; border-radius: 8px; }
  .footer { position: absolute; left: 0; bottom: 0; width: 100%; height: 16px; background: var(--orange); font-size: 6px; color: #fff; display: flex; align-items: center; padding: 0 12px; justify-content: space-between; }
  .footer .cat { font-weight: 800; font-size: 8px; color: var(--ink); }
  .footer .cat em { color: var(--red); font-style: normal; }
  .pnum { background: var(--red); color: #fff; font-weight: 700; padding: 1px 4px; font-size: 6.5px; }

  .edges-photo { position: absolute; left: 0; top: 0; width: 100%; height: 74px; background: linear-gradient(90deg, #b9b2a4, #9aa09b 30%, #b6a8c4 55%, #7f9fb5 75%, #d8d2c8); }
  .edge-band { position: absolute; left: 0; top: 74px; width: 100%; height: 30px; background: var(--orange); display: flex; }
  .edge-band span { flex: 1; font-size: 6px; font-weight: 600; color: var(--ink); padding: 4px 3px; border-right: 1px solid rgba(0,0,0,.25); line-height: 1.2; }
  .edge-band span:last-child { border-right: none; }
</style>
</head>
<body>

<section class="page cover">
  <svg width="560" height="396" viewBox="0 0 560 396">
    <defs>
      <linearGradient id="doorsTone" x1="0" y1="0" x2="1" y2="1">
        <stop offset="0" stop-color="#f1ece3"/><stop offset="1" stop-color="#cfc7ba"/>
      </linearGradient>
      <linearGradient id="windowTone" x1="0" y1="0" x2="1" y2="0">
        <stop offset="0" stop-color="#ffffff"/><stop offset="1" stop-color="#e6e8ea"/>
      </linearGradient>
    </defs>
    <g role="img" aria-label="Photo of white wardrobe doors in a bright room">
      <polygon points="0,0 400,0 330,290 0,290" fill="url(#doorsTone)"/>
    </g>
    <g role="img" aria-label="Faint photo of a white paned window">
      <polygon points="420,0 560,0 560,396 380,396" fill="url(#windowTone)"/>
    </g>
    <rect x="0" y="290" width="360" height="12" fill="#7d7770"/>
    <polygon points="0,302 360,302 340,340 0,340" fill="var(--orange)"/>
    <rect x="0" y="340" width="340" height="56" fill="#8c867f"/>
    <polygon points="200,80 420,80 310,260" fill="var(--beige)" opacity=".92"/>
    <line x1="380" y1="0" x2="460" y2="396" stroke="var(--line)" stroke-width="1"/>
    <line x1="200" y1="0" x2="560" y2="260" stroke="var(--line)" stroke-width="1"/>
    <line x1="560" y1="40" x2="300" y2="396" stroke="#d9d9d9" stroke-width="1"/>
  </svg>
  <div class="cover-brand">Harbour<br>Panels</div>
  <h1 class="cover-title">Custom made<br>kitchen and<br>wardrobe<br>doors</h1>
  <p class="cover-tag">save time and money</p>
</section>

<section class="page page-left">
  <div class="photo-strip" role="img" aria-label="Photo strip of kitchen doors"></div>
  <div class="benefits">
    <ul class="benefit-list">
      <li><b>Save time and money:</b> Competitive prices on every custom kitchen and wardrobe door.</li>
      <li><b>Fast turnaround:</b> Most orders are made and ready within ten working days.</li>
      <li><b>Trade customers:</b> Ask about our trade accounts and volume pricing.</li>
      <li><b>Huge range of designs:</b> Choose from many profiles, edges and finishes.</li>
      <li><b>Top quality:</b> Moisture resistant MDF, cut on modern CNC machines.</li>
      <li><b>Polyurethane painting:</b> Doors can be supplied painted in any colour.</li>
      <li><b>Guarantee:</b> We guarantee the quality and accuracy of all doors.</li>
    </ul>
    <p class="call">Call (02) 9555 0142<span>harbourpanels.com.au</span></p>
  </div>
  <div class="brand">Harbour Panels<small>Kitchen and Wardrobe Doors</small></div>
  <p class="motto">Top Quality, Fast Service</p>
  <div class="badge" role="img" aria-label="Quality certification badge"></div>
  <div class="customise">
    <h2>Customise</h2>
    <h3>your doors</h3>
    <p>Do you want a door that's not featured in our brochure? We can program and produce doors to your specifications.</p>
  </div>
  <p class="range" style="left:236px;top:170px;"><b>RANGE 6000 - 6011</b> Flat panel designs with routed lines for a modern look.</p>
  <div class="doors" style="left:236px;top:188px;">
    <div class="door"><div class="door-img" role="img" aria-label="Door design 6000"></div><span class="door-code">6000 FSQ</span></div>
    <div class="door"><div class="door-img" role="img" aria-label="Door design 6001"></div><span class="door-code">6001 FSQ</span></div>
    <div class="door"><div class="door-img" role="img" aria-label="Door design 6002"></div><span class="door-code">6002 FSQ</span></div>
    <div class="door"><div class="door-img" role="img" aria-label="Door design 6003"></div><span class="door-code">6003 FSQ</span></div>
  </div>
  <div class="footer">
    <span class="pnum">2</span>
    <span>Top Quality, Fast Service · (02) 9555 0142 · sales@harbourpanels.com.au</span>
  </div>
</section>

<section class="page page-right">
  <div class="edges-photo" role="img" aria-label="Close-up photo of painted door edge profiles"></div>
  <div class="edge-band">
    <span>Standard Edge</span><span>Cove Edge</span><span>Medium Cove Edge</span><span>Large Cove Edge</span><span>Pencil Round Edge</span><span>30x3mm Bevelled Edge</span><span>25x5mm Bevelled Edge</span><span>Bevelled with Step Edge</span>
  </div>
  <p class="range" style="left:14px;top:112px;"><b>RANGE 6001</b> Elegant and sophisticated designs for a timeless kitchen.</p>
  <div class="doors" style="left:14px;top:128px;">
    <div class="door"><div class="door-img" role="img" aria-label="Door design 6001 ASQ"></div><span class="door-code">6001 ASQ</span></div>
    <div class="door"><div class="door-img" role="img" aria-label="Door design 6001 BSQ"></div><span class="door-code">6001 BSQ</span></div>
    <div class="door"><div class="door-img" role="img" aria-label="Door design 6001 CSQ"></div><span class="door-code">6001 CSQ</span></div>
    <div class="door"><div class="door-img" role="img" aria-label="Door design 6001 DSQ"></div><span class="door-code">6001 DSQ</span></div>
    <div class="door"><div class="door-img" role="img" aria-label="Door design 6001 ESQ"></div><span class="door-code">6001 ESQ</span></div>
  </div>
  <div class="doors" style="left:14px;top:248px;">
    <div class="door"><div class="door-img" role="img" aria-label="Door design 6001 GSQ"></div><span class="door-code">6001 GSQ</span></div>
    <div class="door"><div class="door-img" role="img" aria-label="Door design 6001 HSQ"></div><span class="door-code">6001 HSQ</span></div>
    <div class="door"><div class="door-img" role="img" aria-label="Door design 6001 KSQ"></div><span class="door-code">6001 KSQ</span></div>
    <div class="door"><div class="door-img" role="img" aria-label="Door design 6001 RSQ"></div><span class="door-code">6001 RSQ</span></div>
    <div class="door"><div class="door-img" role="img" aria-label="Door design 6001 TSQ"></div><span class="door-code">6001 TSQ</span></div>
  </div>
  <div class="footer">
    <span class="cat"><em>product</em> catalogue</span>
    <span class="pnum">3</span>
  </div>
</section>

</body>
</html>
```